Business card design needed with logo

My business is called QVM Solutions & it is targeted towards mobile equipment maintenance in the Mining and civil industry. My work involves maintenance planning and maintenance management plus also supply tradespeople on a labour hire basis. We can provide from basic shut-down machine rebuild plans to complete rebuild services supply plans and labour to anywhere in Australia. I would like to use the colours Black, Red and Grey, I had done a desgin as attached but doesn't really explain what we do and gears don't embroider well onto shirts.
Updates

I also wanted to see the something replace the gears maybe just making the QVM lettering look a bit different or put together differently 

Hello I have extended the deadline by a few extra days as I would like to update details on the front of card, details below & can be put which ever way looks good;

Neil Patton
Director
0417562938
QVM@mailbrook.com.au
www.qvmsolutions-demo.com.au

On the back of the card I would like to have the below printed;

Capable of providing, but not limited to, across Australia:
- Contract Maintenance Planning.
- Skilled Mobile Maintenance labour hire.
- New machine build specifications. 
- Plant risk assessments and inspections.
- Shut down and rebuild program planning.
- Preventative maintenance tasks, including build of materials lists, creation and review.

Target Market(s)

Contractors and companies that use small and large earthmoving and mining machines

Industry/Entity Type

Business

Contact Information for Business Card

Trading name is QVM Solutions
My name and title is
Neil Patton Director
0417 562 938
QVM@mailbrook.com.au

Logo Text

QVM

```html
<!DOCTYPE html>
<html lang="en">
<head>
<meta charset="utf-8">
<title>QVM Solutions – Business Card</title>
<link rel="stylesheet" href="https://fonts.googleapis.com/css2?family=PT+Sans+Narrow:wght@400;700&display=swap">
<style>
  :root {
    --stage-grey: #a3a3a3;
    --card-white: #ffffff;
    --brand-red: #e20c18;
    --deep-red: #c70a14;
    --ink-black: #0b0b0b;
    --rule-grey: #6b6b6b;
    --mark-grey: #8a8a8a;
  }
  html, body {
    margin: 0;
    padding: 0;
    width: 1200px;
    height: 849px;
    overflow: hidden;
    background: var(--stage-grey);
    font-family: "PT Sans Narrow", "Arial Narrow", sans-serif;
  }
  .stage {
    position: relative;
    width: 1200px;
    height: 849px;
  }
  .card {
    position: absolute;
    top: 303px;
    width: 425px;
    height: 242px;
    border-radius: 12px;
    overflow: hidden;
  }
  .card--front { left: 143px; background: var(--card-white); }
  .card--back  { left: 631px; background: var(--brand-red); }

  .card__band {
    position: absolute;
    left: 0;
    bottom: 0;
    width: 100%;
    height: 21px;
  }
  .card--front .card__band { background: var(--brand-red); }
  .card--back .card__band  { background: var(--ink-black); }

  .brand-name {
    position: absolute;
    left: 18px;
    top: 30px;
    display: flex;
    align-items: center;
    gap: 10px;
    color: var(--ink-black);
    font-weight: 400;
    font-size: 40px;
    line-height: 1;
  }
  .brand-name__square {
    width: 22px;
    height: 22px;
    background: var(--mark-grey);
  }
  .trading-name {
    position: absolute;
    left: 209px;
    top: 61px;
    margin: 0;
    color: var(--brand-red);
    font-size: 26px;
    font-weight: 400;
    line-height: 1;
  }
  .contact {
    position: absolute;
    left: 209px;
    top: 128px;
    width: 170px;
    color: var(--ink-black);
  }
  .contact__name {
    margin: 0;
    font-size: 20px;
    line-height: 1;
    padding-bottom: 2px;
    border-bottom: 1px solid var(--rule-grey);
  }
  .contact__title {
    margin: 3px 0 0;
    font-size: 11px;
    line-height: 1;
  }
  .contact__list {
    list-style: none;
    margin: 12px 0 0;
    padding: 0;
    font-size: 11px;
    line-height: 1;
  }
  .contact__item {
    display: flex;
    align-items: center;
    gap: 10px;
    margin-bottom: 6px;
    white-space: nowrap;
  }
  .contact__icon { width: 12px; height: 10px; flex: none; }

  .back-name {
    position: absolute;
    left: 52px;
    top: 88px;
    margin: 0;
    color: var(--ink-black);
    font-size: 40px;
    font-weight: 400;
    line-height: 1;
  }
  .back-graphic {
    position: absolute;
    left: 229px;
    top: 0;
    width: 158px;
    height: 221px;
    background: linear-gradient(180deg, var(--deep-red), var(--brand-red));
  }
</style>
</head>
<body>
<main class="stage">

  <section class="card card--front" aria-label="Card front">
    <div class="brand-name">
      <span class="brand-name__text">QVM</span>
      <span class="brand-name__square"></span>
    </div>
    <h1 class="trading-name">QVM Solutions</h1>
    <div class="contact">
      <p class="contact__name">Neil Patton</p>
      <p class="contact__title">Director</p>
      <ul class="contact__list">
        <li class="contact__item">
          <svg class="contact__icon" viewBox="0 0 12 10" aria-hidden="true">
            <path d="M2 1 L4 1 L5 3 L4 4 Q5 6 7 7 L8 6 L10 7 L10 9 Q4 9 2 1 Z" fill="#0b0b0b"/>
          </svg>
          <span>0417 562 938</span>
        </li>
        <li class="contact__item">
          <svg class="contact__icon" viewBox="0 0 12 10" aria-hidden="true">
            <rect x="0.5" y="1.5" width="11" height="7" fill="#0b0b0b"/>
            <path d="M1 2 L6 6 L11 2" stroke="#fff" stroke-width="1" fill="none"/>
          </svg>
          <span>e-mail : QVM@mailbrook.com.au</span>
        </li>
      </ul>
    </div>
    <div class="card__band"></div>
  </section>

  <section class="card card--back" aria-label="Card back">
    <div class="back-graphic" role="img" aria-label="Large outlined machinery decoration"></div>
    <h2 class="back-name">QVM Solutions</h2>
    <div class="card__band"></div>
  </section>

</main>
</body>
</html>
```